New Company Business Card Design

I have a new company logo and I want a new business card design. I dont know if the logo file i attached is in the correct format or quality. We are a New York City Specialty construction Firm specializing in high risk out of the box projects. I want a simple and classy business card that people will his card is as crisp as the work his company does.

Target Market(s)

Clients in the heavy construction industry in New York City

Industry/Entity Type

Construction Company

Contact Information for Business Card

Simple Classy - DIFFERENT

Font styles to use
Other font styles liked:
• Mach the logo font in some way

Colors

Designer to choose colors to be used in the design.

Requirements
Must have
• Uniqueness
Nice to have
• Nothing particular - Just different and classy - Timeless
Should not have
• Goofy Shit or Gimmicky shit

```html
<!DOCTYPE html>
<html lang="en">
<head>
<meta charset="utf-8">
<title>KVR Associates, Inc. – Business Card</title>
<link rel="stylesheet" href="https://fonts.googleapis.com/css2?family=Roboto:wght@400;700;900&display=swap">
<style>
  :root {
    --backdrop: #e6e6e6;
    --card: #ffffff;
    --navy: #0d4a8f;
    --sky: #0aa3e2;
    --ink: #141414;
    --muted: #444444;
  }
  * { margin: 0; padding: 0; box-sizing: border-box; }
  html, body { width: 1200px; height: 1000px; overflow: hidden; }
  body {
    background: var(--backdrop);
    font-family: "Roboto", Arial, sans-serif;
    position: relative;
  }
  .card {
    position: absolute;
    background: var(--card);
    width: 714px;
    height: 408px;
    overflow: hidden;
  }
  .card--front { left: 242px; top: 62px; }
  .card--back { left: 244px; top: 530px; }

  .name-accent {
    position: absolute; left: 0; top: 16px;
    width: 24px; height: 74px; background: var(--sky);
  }
  .holder-name {
    position: absolute; left: 36px; top: 31px;
    font-size: 30px; font-weight: 400; color: var(--navy);
  }

  .contact-list { list-style: none; position: absolute; left: 32px; top: 117px; }
  .contact-item {
    display: flex; align-items: flex-start;
    height: 45px; font-size: 22px; color: var(--ink);
  }
  .contact-item--address { color: var(--muted); line-height: 36px; margin-top: -7px; }
  .contact-icon { width: 26px; height: 26px; margin-right: 27px; flex: none; }
  .contact-item--address .contact-icon { margin-top: 5px; }

  .wordmark {
    position: absolute; right: 18px; top: 50px;
    width: 250px; text-align: center;
    color: var(--sky); font-weight: 900;
  }
  .wordmark__name { display: block; font-size: 78px; line-height: 0.95; letter-spacing: 2px; }
  .wordmark__suffix { display: block; font-size: 15px; letter-spacing: 5px; margin-top: 8px; }

  .footer-bands { position: absolute; left: 0; bottom: 0; width: 714px; height: 42px; }
  .footer-url {
    position: absolute; left: 94px; bottom: 10px;
    font-size: 21px; color: #ffffff;
  }

  .wordmark--large {
    right: auto; left: 157px; top: 132px; width: 400px;
  }
  .wordmark--large .wordmark__name { font-size: 118px; }
  .wordmark--large .wordmark__suffix { font-size: 19px; letter-spacing: 7px; margin-top: 14px; }

  .back-footer {
    position: absolute; left: 24px; top: 366px; width: 667px;
    display: flex; align-items: center; gap: 8px;
  }
  .back-rule { flex: 1; height: 2px; background: var(--sky); }
  .back-url {
    flex: none; font-size: 26px; line-height: 32px; color: var(--navy);
  }
</style>
</head>
<body>

<section class="card card--front">
  <div class="name-accent"></div>
  <h1 class="holder-name">Marcus T. Bellamy</h1>

  <ul class="contact-list">
    <li class="contact-item">
      <svg class="contact-icon" viewBox="0 0 26 26" aria-hidden="true">
        <circle cx="13" cy="13" r="13" fill="var(--navy)"/>
        <path d="M6 11c0-3 14-3 14 0v1.5h-3.5v-1.8c-2-.8-5-.8-7 0v1.8H6z" fill="#fff"/>
        <rect x="8" y="13" width="10" height="6" rx="1.5" fill="#fff"/>
      </svg>
      <span>555-014-2287</span>
    </li>
    <li class="contact-item">
      <svg class="contact-icon" viewBox="0 0 26 26" aria-hidden="true">
        <circle cx="13" cy="13" r="13" fill="var(--navy)"/>
        <path d="M9 6.5l2.3 3.6-1.6 1.6c.9 2 2.6 3.7 4.6 4.6l1.6-1.6 3.6 2.3-1.4 2.6c-5.6-.4-10.1-4.9-10.5-10.5z" fill="#fff"/>
      </svg>
      <span>555-013-7740</span>
    </li>
    <li class="contact-item">
      <svg class="contact-icon" viewBox="0 0 26 26" aria-hidden="true">
        <circle cx="13" cy="13" r="13" fill="var(--navy)"/>
        <rect x="7" y="8.5" width="12" height="9" rx="1" fill="none" stroke="#fff" stroke-width="1.8"/>
        <path d="M7.5 9.5l5.5 4.2 5.5-4.2" fill="none" stroke="#fff" stroke-width="1.8"/>
      </svg>
      <span>marcus@kvrbuild.com</span>
    </li>
    <li class="contact-item contact-item--address">
      <svg class="contact-icon" viewBox="0 0 26 26" aria-hidden="true">
        <circle cx="13" cy="13" r="13" fill="var(--navy)"/>
        <path d="M13 6.5l6.5 6h-2v6h-3.2v-4h-2.6v4H8.5v-6h-2z" fill="#fff"/>
      </svg>
      <span>118 Harbor Mill Road -<br>Linden Point, New Jersey 07999</span>
    </li>
  </ul>

  <div class="wordmark">
    <span class="wordmark__name">KVR</span>
    <span class="wordmark__suffix">ASSOCIATES, INC.</span>
  </div>

  <svg class="footer-bands" viewBox="0 0 714 42" aria-hidden="true">
    <polygon points="0,0 300,0 336,42 0,42" fill="var(--navy)"/>
    <polygon points="326,16 714,16 714,42 350,42" fill="var(--sky)"/>
  </svg>
  <span class="footer-url">www.kvrbuild.com</span>
</section>

<section class="card card--back">
  <div class="wordmark wordmark--large">
    <span class="wordmark__name">KVR</span>
    <span class="wordmark__suffix">ASSOCIATES, INC.</span>
  </div>
  <div class="back-footer">
    <span class="back-rule"></span>
    <p class="back-url">www.kvrbuild.com</p>
    <span class="back-rule"></span>
  </div>
</section>

</body>
</html>
```